Crestline Marketing Business Card

Business card using new logo for marketing consulting company based in Silicon Valley. Limited information on card now (name, phone number, email, website), but room to add mailing address later.

```html
<!DOCTYPE html>
<html lang="en">
<head>
<meta charset="utf-8">
<title>Crestline Marketing Business Card</title>
<link rel="stylesheet" href="https://fonts.googleapis.com/css2?family=Lato:wght@100;300;400;700;900&family=Lobster&display=swap">
<style>
  :root {
    --sky: #00aef8;
    --band: #00bdfc;
    --ink: #000000;
    --paper: #ffffff;
    --aqua: #3ff2f7;
    --cobalt: #1769f2;
    --text: #111111;
  }
  html, body {
    margin: 0;
    padding: 0;
    overflow: hidden;
    background: var(--paper);
  }
  .canvas {
    position: relative;
    width: 1050px;
    height: 1200px;
    overflow: hidden;
    font-family: "Lato", sans-serif;
  }
  .backdrop {
    position: absolute;
    inset: 0;
  }
  .side-label {
    position: absolute;
    left: 36px;
    margin: 0;
    font-family: "Lobster", cursive;
    font-weight: 400;
    font-size: 40px;
    letter-spacing: 9px;
    color: var(--paper);
  }
  .side-label--front { top: 24px; }
  .side-label--back { top: 636px; }

  .brand {
    position: absolute;
    margin: 0;
    font-family: "Lato", sans-serif;
    font-weight: 400;
    color: var(--aqua);
    text-transform: uppercase;
    text-align: center;
    line-height: 1.05;
  }
  .brand--front {
    left: 20px;
    width: 380px;
    top: 270px;
    font-size: 42px;
  }
  .brand--back {
    left: 0;
    width: 1050px;
    top: 940px;
    font-size: 74px;
  }

  .holder-name {
    position: absolute;
    right: 48px;
    top: 128px;
    margin: 0;
    font-size: 56px;
    color: var(--paper);
    letter-spacing: 1px;
  }
  .holder-name__first { font-weight: 900; }
  .holder-name__last { font-weight: 100; }

  .mailing {
    position: absolute;
    left: 700px;
    width: 312px;
    top: 271px;
    margin: 0;
    text-align: center;
    font-size: 21px;
    color: var(--text);
  }
  .contact {
    position: absolute;
    right: 130px;
    margin: 0;
    text-align: right;
    font-size: 21px;
    line-height: 31px;
    color: var(--text);
  }
  .contact--phone { top: 393px; }
  .contact--web { top: 502px; }
</style>
</head>
<body>
<main class="canvas">
  <svg class="backdrop" width="1050" height="1200" viewBox="0 0 1050 1200" aria-hidden="true">
    <defs>
      <linearGradient id="rule-fade" x1="0" x2="1" y1="0" y2="0">
        <stop offset="0" stop-color="#00c8ff" stop-opacity="0"/>
        <stop offset="0.5" stop-color="#00b4ff"/>
        <stop offset="1" stop-color="#1769f2"/>
      </linearGradient>
    </defs>
    <!-- front side -->
    <rect x="0" y="0" width="1050" height="600" fill="var(--paper)"/>
    <polygon points="0,0 340,0 476,240 278,600 0,600" fill="var(--sky)"/>
    <polygon points="356,0 1050,0 1050,240 487,240" fill="var(--ink)"/>
    <circle cx="210" cy="178" r="66" fill="var(--aqua)"/>

    <!-- phone row -->
    <rect x="640" y="424" width="292" height="2" fill="url(#rule-fade)"/>
    <polygon points="948,389 990,389 1010,425 990,461 948,461 928,425" fill="var(--cobalt)"/>
    <g class="icon-phone" fill="var(--paper)">
      <path d="M952,416 q17,-10 34,0 l0,5 -7,0 0,-4 q-10,-4 -20,0 l0,4 -7,0z"/>
      <rect x="956" y="422" width="26" height="17" rx="2"/>
    </g>
    <g fill="var(--cobalt)">
      <rect x="963" y="426" width="3" height="2"/><rect x="968" y="426" width="3" height="2"/><rect x="973" y="426" width="3" height="2"/>
      <rect x="963" y="430" width="3" height="2"/><rect x="968" y="430" width="3" height="2"/><rect x="973" y="430" width="3" height="2"/>
      <rect x="963" y="434" width="3" height="2"/><rect x="968" y="434" width="3" height="2"/><rect x="973" y="434" width="3" height="2"/>
    </g>

    <!-- web row -->
    <rect x="640" y="531" width="292" height="2" fill="url(#rule-fade)"/>
    <polygon points="948,495 990,495 1010,531 990,567 948,567 928,531" fill="var(--cobalt)"/>
    <g class="icon-monitor" fill="var(--paper)">
      <path d="M951,516 h36 v25 h-36z M955,520 v17 h28 v-17z" fill-rule="evenodd"/>
      <rect x="966" y="541" width="6" height="5"/>
      <rect x="960" y="546" width="18" height="3"/>
    </g>

    <!-- back side -->
    <rect x="0" y="600" width="1050" height="530" fill="var(--ink)"/>
    <rect x="0" y="1130" width="1050" height="70" fill="var(--band)"/>
    <circle cx="525" cy="790" r="118" fill="var(--aqua)"/>
  </svg>

  <h2 class="side-label side-label--front">Front Side</h2>
  <p class="brand brand--front">Crestline<br>Marketing</p>

  <h1 class="holder-name"><span class="holder-name__first">YOUR</span> <span class="holder-name__last">NAME</span></h1>
  <p class="mailing">Mailing Address</p>
  <p class="contact contact--phone">Mobile<br>Office</p>
  <p class="contact contact--web">Email<br>Website</p>

  <h2 class="side-label side-label--back">Back Side</h2>
  <p class="brand brand--back">Crestline Marketing</p>
</main>
</body>
</html>
```